quarry productions business cards design

design a clean look but creative business card for a production company, I'm a freelance producer and launching my startup, would like to keep a clean professional look but still creative

Target Market(s)

businesses

Industry/Entity Type

video production

Contact Information for Business Card

logo, name (Karl Benn), Title (Producer), (MFA Filmmaking, QTSA Los Angeles), contact number & email ID

Colors

Designer to choose only greyscale colors for use in the design.

Requirements
Must have
• logo, black and white colors, you can play with their shades
Nice to have
• a unique design, not necessarily a typical size card
Should not have
• too colorful or playful

```html
<!DOCTYPE html>
<html lang="en">
<head>
<meta charset="UTF-8">
<title>Quarry Productions — Business Cards</title>
<link href="https://fonts.googleapis.com/css2?family=Outfit:wght@300;400;500;700&display=swap" rel="stylesheet">
<style>
  :root {
    --bg-edge: #b9b9b9;
    --bg-centre: #ececec;
    --card-light: #ffffff;
    --card-dark: #2a2a2b;
    --ink-black: #000000;
    --ink-white: #ffffff;
    --ink-grey: #6e6e6e;
    --icon-grey: #8c8c8c;
  }
  * { margin: 0; padding: 0; box-sizing: border-box; }
  html, body {
    width: 1200px;
    height: 1200px;
    overflow: hidden;
  }
  body {
    background: linear-gradient(90deg, var(--bg-edge) 0%, var(--bg-centre) 50%, var(--bg-edge) 100%);
    font-family: "Outfit", sans-serif;
    display: flex;
    align-items: center;
    justify-content: center;
  }
  .card-set {
    display: flex;
    gap: 60px;
  }
  .card {
    width: 500px;
    height: 500px;
    position: relative;
  }

  /* Front */
  .card-front {
    background: var(--card-light);
    display: flex;
    align-items: center;
    justify-content: center;
  }
  .front-wordmark {
    color: var(--ink-black);
    font-weight: 700;
    font-size: 40px;
    letter-spacing: 1px;
    text-transform: uppercase;
    text-align: center;
    line-height: 1.05;
  }

  /* Back */
  .card-back {
    background: var(--card-dark);
    color: var(--ink-white);
  }
  .back-frame {
    position: absolute;
    left: 59px;
    right: 58px;
    top: 62px;
    bottom: 58px;
    border: 1.5px solid var(--ink-white);
  }
  .back-content {
    position: absolute;
    inset: 0;
    display: flex;
    flex-direction: column;
    align-items: center;
    padding-top: 44px;
    text-align: center;
  }
  .company-title {
    background: var(--card-dark);
    padding: 0 8px;
    font-weight: 700;
    font-size: 34px;
    line-height: 0.98;
    text-transform: uppercase;
    letter-spacing: -0.3px;
  }
  .company-title .line-two { display: block; padding: 0 0; }
  .person-name {
    margin-top: 42px;
    font-weight: 700;
    font-size: 22px;
    letter-spacing: 0.5px;
    text-transform: uppercase;
  }
  .person-role,
  .person-degree {
    font-weight: 400;
    font-size: 14.5px;
    letter-spacing: 1.3px;
    margin-top: 4px;
  }
  .back-wordmark {
    margin-top: 36px;
    color: var(--ink-grey);
    font-weight: 700;
    font-size: 17px;
    letter-spacing: 1px;
    text-transform: uppercase;
  }
  .contact-icons {
    margin-top: 36px;
    display: flex;
    gap: 12px;
  }
  .contact-icons svg { width: 14px; height: 14px; }
  .contact-lines {
    margin-top: 8px;
    font-size: 13.5px;
    font-weight: 400;
    line-height: 1.08;
  }
  .contact-lines p + p.spaced { margin-top: 6px; }
</style>
</head>
<body>
  <main class="card-set">
    <section class="card card-front" aria-label="Card front">
      <div class="front-wordmark">Quarry<br>Productions</div>
    </section>

    <section class="card card-back" aria-label="Card back">
      <div class="back-frame"></div>
      <div class="back-content">
        <h1 class="company-title">Quarry<span class="line-two">Productions</span></h1>
        <h2 class="person-name">Karl Benn</h2>
        <p class="person-role">Producer</p>
        <p class="person-degree">MFA Filmmaking, QTSA Los Angeles</p>

        <div class="back-wordmark">Quarry Productions</div>

        <div class="contact-icons" aria-hidden="true">
          <svg viewBox="0 0 16 16"><path fill="var(--icon-grey)" d="M8 1a5 5 0 0 0-5 5c0 3.6 5 9 5 9s5-5.4 5-9a5 5 0 0 0-5-5zm0 7a2 2 0 1 1 0-4 2 2 0 0 1 0 4z"/></svg>
          <svg viewBox="0 0 16 16"><path fill="var(--icon-grey)" d="M4.2 1.5l2 2.6-1.2 1.6c.9 2 2.4 3.5 4.4 4.4l1.6-1.2 2.6 2-1.2 2.4C7.3 13.6 2.4 8.7 1.8 3.6z"/></svg>
          <svg viewBox="0 0 16 16"><rect x="1.5" y="3.5" width="13" height="9" fill="none" stroke="var(--icon-grey)" stroke-width="1.6"/><path d="M1.5 3.5 8 9l6.5-5.5" fill="none" stroke="var(--icon-grey)" stroke-width="1.6"/></svg>
        </div>

        <div class="contact-lines">
          <p>345 Street No. City, State</p>
          <p>Zip, Country</p>
          <p class="spaced">+0123 4567 9000</p>
          <p class="spaced">youremailname@mail.com</p>
        </div>
      </div>
    </section>
  </main>
</body>
</html>
```